Book cover for modern/pop-culture-oriented poetry collection

We need a simple, streamlined book-cover design (that'll ultimately be 1600 x 2500 pixels; 300 dpi) for a book of poems. We would like to see three elements on the cover: (1) the title in all caps (GLASSHOURS); (2) the author name in all caps (MIRA TOLLEN); (3) the main image (attached, slugged "glasshours image"). Image and text should be centered on the cover.

Target Market(s)

Readers of contemporary poetry

Font styles to use
Sans Serif

Requirements
Must have
• Book title, author name, attached photo
Nice to have
• Also attached is the cover of a book (HARBOUR) that is in the style/spirit of what we're looking for.

```html
<!DOCTYPE html>
<html lang="en">
<head>
<meta charset="UTF-8">
<title>GLASSHOURS — Mira Tollen</title>
<link rel="stylesheet" href="https://fonts.googleapis.com/css2?family=Oswald:wght@400;500&display=swap">
<style>
  :root {
    --cover-paper: #efebe8;
    --title-ink: #1f1a17;
    --author-ink: #9b9896;
    --image-wood: #6b5444;
    --image-grey: #a9aaa3;
    --image-light: #e2deda;
  }
  html, body {
    margin: 0;
    padding: 0;
    width: 886px;
    height: 1200px;
    overflow: hidden;
    background: var(--cover-paper);
  }
  .book-cover {
    position: relative;
    width: 886px;
    height: 1200px;
    background: var(--cover-paper);
    font-family: "Oswald", sans-serif;
  }
  .book-title {
    position: absolute;
    top: 232px;
    left: 0;
    width: 100%;
    margin: 0;
    text-align: center;
    font-weight: 500;
    font-size: 124px;
    line-height: 1;
    letter-spacing: 0.03em;
    color: var(--title-ink);
  }
  .cover-image {
    position: absolute;
    left: 215px;
    top: 385px;
    width: 490px;
    height: 585px;
    background: linear-gradient(180deg, var(--image-light) 0%, var(--image-wood) 30%, var(--image-grey) 60%, var(--image-light) 100%);
  }
  .author-name {
    position: absolute;
    top: 1010px;
    left: 0;
    width: 100%;
    margin: 0;
    text-align: center;
    font-weight: 400;
    font-size: 64px;
    line-height: 1;
    letter-spacing: 0.04em;
    color: var(--author-ink);
  }
</style>
</head>
<body>
  <main class="book-cover">
    <h1 class="book-title">GLASSHOURS</h1>
    <div class="cover-image" role="img" aria-label="glasshours image: vintage wood-cabinet television on tapered legs"></div>
    <p class="author-name">MIRA TOLLEN</p>
  </main>
</body>
</html>
```